Latin CBD company needs a design for a counter display box

-We would like a design for a display box for our restorative CBD oil tinctures. We would like to stand out our brand promoting wellness being and health. However, because its targeting the latin market, we would like to see color on it.
- The display box is for CBD tinctures (image attached)
-I am attaching two files, if you are Spanish speaker it would be nice to see the design in Spanish. Thank you!
THANK YOU IN ADVANCE FOR WORKING IN OUR PROJECT!

Font styles to use
Serif
Sans Serif

```html
<!DOCTYPE html>
<html lang="es">
<head>
<meta charset="utf-8">
<title>Soleva CBD – Caja de exhibición</title>
<link href="https://fonts.googleapis.com/css2?family=PT+Sans:wght@400;700&family=Didact+Gothic&display=swap" rel="stylesheet">
<style>
  :root {
    --bg: #e6dfde;
    --green: #7cb83a;
    --green-light: #9fd25a;
    --green-pale: #e6f3d2;
    --white: #f7f7f5;
    --ink: #3d3d3d;
  }
  * { box-sizing: border-box; margin: 0; padding: 0; }
  html, body { width: 1200px; height: 900px; overflow: hidden; background: var(--bg); }
  .canvas { position: relative; width: 1200px; height: 900px; display: flex; justify-content: center; align-items: center; }
  .box { display: flex; height: 760px; box-shadow: 0 10px 30px rgba(0,0,0,0.12); }
  .panel { position: relative; height: 100%; background: var(--white); display: flex; flex-direction: column; overflow: hidden; }
  .panel--side { width: 260px; border-right: 1px solid #dcdcdc; }
  .panel--front { width: 400px; }
  .top-strip { height: 38px; background: linear-gradient(90deg, var(--green-light), var(--green)); flex: none; }
  .brand { display: flex; flex-direction: column; align-items: center; gap: 12px; font-family: "PT Sans", sans-serif; color: var(--green); }
  .brand__dot { border: 3px solid var(--green); border-radius: 50%; }
  .panel--front .brand { padding-top: 40px; height: 262px; }
  .panel--front .brand__dot { width: 70px; height: 70px; }
  .panel--front .brand__name { font-size: 46px; }
  .title-band { background: var(--green); color: #fff; text-align: center; font-family: "PT Sans", sans-serif; padding: 22px 16px 24px; }
  .title-band__name { font-size: 36px; font-weight: 700; line-height: 1.2; }
  .title-band__sub { font-family: "Didact Gothic", sans-serif; font-size: 20px; margin-top: 14px; }
  .meadow { position: relative; flex: 1; background: linear-gradient(180deg, var(--white) 0%, var(--green-pale) 40%, var(--green-light) 100%); }
  .meadow__content { position: absolute; inset: 0; display: flex; flex-direction: column; align-items: center; text-align: center; font-family: "Didact Gothic", sans-serif; color: var(--ink); }
  .tagline { margin-top: 48px; font-size: 21px; letter-spacing: 3px; line-height: 1.35; }
  .amount { margin-top: auto; font-size: 20px; line-height: 2; margin-bottom: 40px; }
  .panel--side .brand { padding-top: 36px; }
  .panel--side .brand__dot { width: 40px; height: 40px; border-width: 2px; }
  .panel--side .brand__name { font-size: 24px; }
  .side-title { text-align: center; font-family: "PT Sans", sans-serif; color: var(--green); margin-top: 26px; }
  .side-title__name { font-size: 18px; font-weight: 700; }
  .side-title__sub { font-size: 12px; margin-top: 4px; }
  .features { list-style: none; font-family: "PT Sans", sans-serif; font-size: 12.5px; color: var(--ink); padding: 22px 22px 0; line-height: 1.35; }
  .features li { margin-bottom: 8px; }
  .features li::before { content: "• "; }
  .about { font-family: "PT Sans", sans-serif; font-size: 8.5px; color: var(--ink); padding: 6px 22px 0; line-height: 1.4; }
  .about p { margin-bottom: 8px; }
  .age-badge { position: absolute; right: 14px; bottom: 24px; width: 26px; height: 26px; border-radius: 50%; background: #fff; border: 3px solid #d9322b; }
</style>
</head>
<body>
<main class="canvas">
  <div class="box">
    <section class="panel panel--side">
      <div class="top-strip"></div>
      <div class="brand">
        <span class="brand__dot"></span>
        <span class="brand__name">SOLEVA CBD</span>
      </div>
      <div class="side-title">
        <div class="side-title__name">Aceite Restaurador de CBD</div>
        <div class="side-title__sub">Hemp Oil Extract</div>
      </div>
      <ul class="features">
        <li>100% Colorado Grown Organic Hemp.</li>
        <li>Promote a healthy Endocannabinoid System.</li>
        <li>Full Spectrum.</li>
        <li>Non Psicoactive.</li>
      </ul>
      <div class="meadow" role="img" aria-label="Soft green background with faint hemp leaves and flowing light waves">
        <div class="about">
          <p>Our company was born in the high mountain valleys, where a small team of growers shares a passion for natural wellness and a balanced, healthy daily routine for every family.</p>
          <p>We test every batch in certified labs and share the results openly, so you always know what is inside each bottle and can trust its quality.</p>
        </div>
        <span class="age-badge"></span>
      </div>
    </section>
    <section class="panel panel--front">
      <div class="top-strip"></div>
      <div class="brand">
        <span class="brand__dot"></span>
        <span class="brand__name">SOLEVA CBD</span>
      </div>
      <div class="title-band">
        <div class="title-band__name">Aceite Restaurador<br>de CBD</div>
        <div class="title-band__sub">Hemp Oil Extract</div>
      </div>
      <div class="meadow" role="img" aria-label="Soft green background with faint hemp leaves and flowing light waves">
        <div class="meadow__content">
          <p class="tagline">ENJOY THE BENEFITS OF<br>HEALTHY LIVING</p>
          <p class="amount">300mg CBD<br>1FlOz(30ml)</p>
        </div>
      </div>
    </section>
  </div>
</main>
</body>
</html>
```